K&T Fixit and Rebuild general contracting business card design

I already have a logo that I want to use and I need a card that uses that logo and color scheme on the front with the address phone numbers and email and on the back a place for technicians to write in their name and phone number when they hand it out. It will need the License number of License #KTFXTRB318QN.
It should say General Contractor under the company name. The address is
4417 NE 3rd St, Ste D226
Vancouver, WA 98652
www.kandtfixitandrebuild.example
office@kandtfixitandrebuild.example
360-555-0142 is the telephone number
360-555-0187 is the fax number

Target Market(s)

Homeowners needing remodel work or repairs in their home.

Industry/Entity Type

Construction

Contact Information for Business Card

Business name, address, phone number, license number, fax number, email, and website on the front and a place to fill in technician's name and number

Font styles to use
Serif

Requirements
Must have
• Business name, address, phone number, license number, fax number, email, and website on the front and a place to fill in technician's name and number
Nice to have
• I uploaded an example of a front that is good.
Should not have
• Froo froo or extra embellishments.

```html
<!DOCTYPE html>
<html lang="en">
<head>
<meta charset="utf-8">
<title>K&amp;T Fixit and Rebuild – Business Card</title>
<link rel="stylesheet" href="https://fonts.googleapis.com/css2?family=Libre+Baskerville:wght@400;700&display=swap">
<style>
  :root {
    --maroon: #6b1027;
    --maroon-dark: #560b1f;
    --ink-grey: #5f5f5f;
    --card-white: #ffffff;
    --stage: #3b3b3b;
    --on-maroon: #ffffff;
    --on-maroon-soft: rgba(255,255,255,0.82);
  }
  * { box-sizing: border-box; margin: 0; padding: 0; }
  html, body { width: 1200px; height: 900px; overflow: hidden; }
  body {
    background: var(--stage);
    font-family: "Libre Baskerville", Georgia, serif;
    position: relative;
  }
  .card {
    position: absolute;
    width: 520px;
    height: 297px;
    border-radius: 3px;
    box-shadow: 0 10px 28px rgba(0,0,0,0.45);
  }

  /* Front */
  .card-front {
    left: 50px;
    top: 420px;
    background: var(--card-white);
  }
  .card-front .brand-name {
    position: absolute;
    left: 30px;
    top: 22px;
    font-weight: 700;
    font-size: 21px;
    color: var(--maroon);
  }
  .card-front .brand-tagline {
    position: absolute;
    left: 30px;
    top: 54px;
    font-size: 11px;
    letter-spacing: 2px;
    text-transform: uppercase;
    color: var(--ink-grey);
  }
  .person-name {
    position: absolute;
    right: 30px;
    top: 80px;
    font-size: 17px;
    letter-spacing: 2px;
    color: var(--maroon);
  }
  .divider {
    position: absolute;
    left: 30px;
    right: 30px;
    top: 106px;
    height: 1px;
    background: var(--maroon);
  }
  .person-title {
    position: absolute;
    right: 30px;
    top: 113px;
    font-size: 11px;
    font-style: italic;
    color: var(--ink-grey);
  }
  .contact-list {
    position: absolute;
    left: 30px;
    top: 122px;
    list-style: none;
  }
  .contact-list li {
    display: flex;
    align-items: center;
    gap: 7px;
    font-size: 11px;
    color: var(--ink-grey);
    line-height: 20px;
  }
  .contact-list svg { width: 10px; height: 10px; fill: var(--maroon); flex: none; }
  .license {
    position: absolute;
    left: 30px;
    bottom: 30px;
    font-size: 11px;
    font-weight: 700;
    color: var(--maroon);
  }
  .address {
    position: absolute;
    right: 30px;
    bottom: 30px;
    text-align: right;
    font-size: 12px;
    line-height: 19px;
    color: var(--ink-grey);
  }

  /* Back */
  .card-back {
    left: 630px;
    top: 110px;
    background: linear-gradient(160deg, var(--maroon) 0%, var(--maroon-dark) 100%);
    padding: 40px 50px 0;
    text-align: center;
  }
  .card-back .brand-name {
    font-weight: 700;
    font-size: 27px;
    color: var(--on-maroon);
  }
  .card-back .brand-tagline {
    margin-top: 8px;
    font-size: 11px;
    letter-spacing: 3px;
    text-transform: uppercase;
    color: var(--on-maroon-soft);
  }
  .write-in {
    margin-top: 42px;
    display: flex;
    flex-direction: column;
    gap: 26px;
  }
  .write-in-field {
    display: flex;
    align-items: flex-end;
    gap: 10px;
    font-size: 12px;
    color: var(--on-maroon);
    text-align: left;
  }
  .write-in-label { width: 86px; flex: none; }
  .write-in-line {
    flex: 1;
    height: 1px;
    background: var(--on-maroon-soft);
    margin-bottom: 3px;
  }
</style>
</head>
<body>
  <section class="card card-front" aria-label="Business card front">
    <div class="brand-name">K&amp;T Fixit and Rebuild</div>
    <div class="brand-tagline">General Contractor</div>
    <div class="person-name">DANIEL REYES</div>
    <div class="divider"></div>
    <div class="person-title">Director</div>
    <ul class="contact-list">
      <li>
        <svg viewBox="0 0 10 10" aria-hidden="true"><path d="M2 0.5 L3.8 2.6 L3 3.8 Q4.2 6 6.2 7 L7.4 6.2 L9.5 8 L8.2 9.5 Q3.5 9 0.5 1.8 Z"/></svg>
        Tel 360-555-0142
      </li>
      <li>
        <svg viewBox="0 0 10 10" aria-hidden="true"><rect x="1" y="4" width="8" height="5" rx="1"/><rect x="2.5" y="0.5" width="5" height="3"/></svg>
        Fax 360-555-0187
      </li>
      <li>
        <svg viewBox="0 0 10 10" aria-hidden="true"><path d="M0.5 2 H9.5 V8.5 H0.5 Z M1.5 3 L5 5.8 L8.5 3" fill="none" stroke="#6b1027" stroke-width="1.1"/></svg>
        office@kandtfixitandrebuild.example
      </li>
      <li>
        <svg viewBox="0 0 10 10" aria-hidden="true"><circle cx="5" cy="5" r="4.3" fill="none" stroke="#6b1027" stroke-width="1.1"/><path d="M0.7 5 H9.3 M5 0.7 Q2.5 5 5 9.3 M5 0.7 Q7.5 5 5 9.3" fill="none" stroke="#6b1027" stroke-width="0.8"/></svg>
        www.kandtfixitandrebuild.example
      </li>
    </ul>
    <div class="license">License #KTFXTRB318QN</div>
    <div class="address">4417 NE 3rd St, Ste D226<br>Vancouver, WA 98652</div>
  </section>

  <section class="card card-back" aria-label="Business card back">
    <div class="brand-name">K&amp;T Fixit and Rebuild</div>
    <div class="brand-tagline">General Contractor</div>
    <div class="write-in">
      <div class="write-in-field"><span class="write-in-label">Technician</span><span class="write-in-line"></span></div>
      <div class="write-in-field"><span class="write-in-label">Phone</span><span class="write-in-line"></span></div>
    </div>
  </section>
</body>
</html>
```